Grand Opening / Live Music Event

My band is playing a Grand Opening event on Saturday April 5th. I need a flyer utilizing the attached image of our bass player and incorporating our band logo. This picture makes me laugh and gives the impression he is angry - like saying "it's going to be a celebration fool!" or something along those lines. I need to the flyer to pop and present an image that it will be an excellent party. Feel free to incorporate any background or theme style. You can find other images of my band in the event they are needed at: https://www.velorumhub.example/Corkvalleyband

Some details:

The event will be at Quimby's Hall. 8241 Larkspur Ave. #204, Frisco, Texas. (214) 705-9183 for table reservations.

Saturday April 5th. Party starts at 7:00 PM with an acoustic set by the Velvet Otters and Cork Valley taking the stage at 10:00 PM.

Hottest new bar in Frisco! Drink specials all night with the Zephyr Pale girls, and great live music to celebrate this grand opening.

I will use this for FB and other online marketing, as well as some print.

```html
<!DOCTYPE html>
<html lang="en">
<head>
<meta charset="utf-8">
<title>Cork Valley Live – Grand Opening at Quimby's Hall</title>
<link href="https://fonts.googleapis.com/css2?family=Open+Sans:wght@400;600&family=Rubik+Wet+Paint&family=Rubik+Dirt&display=swap" rel="stylesheet">
<style>
  :root {
    --paper: #ffffff;
    --frame: #e4e4e4;
    --night: #2b2a2a;
    --ink: #1d1d1d;
    --chalk: #ffffff;
    --signal-red: #e0233a;
    --stage-blue: #1b2a5c;
    --stage-pink: #e04a8c;
    --stage-red: #d8253a;
  }
  * { margin: 0; padding: 0; box-sizing: border-box; }
  html, body { width: 1200px; height: 860px; overflow: hidden; background: var(--paper); }
  .flyer {
    position: relative;
    width: 1200px; height: 860px;
    background: var(--paper);
    border: 2px solid var(--frame);
    overflow: hidden;
    font-family: "Open Sans", sans-serif;
  }
  .backdrop { position: absolute; inset: 0; }
  .band-photo {
    position: absolute;
    left: 57px; top: 50px; width: 480px; height: 680px;
    background:
      radial-gradient(ellipse at 40% 40%, var(--stage-red) 0%, transparent 35%),
      radial-gradient(ellipse at 45% 80%, var(--stage-pink) 0%, transparent 45%),
      linear-gradient(160deg, #0e1128 0%, var(--stage-blue) 45%, #3a1a3d 100%);
    clip-path: polygon(0 0, 100% 0, 100% 79%, 57% 79%, 44% 100%, 0 100%);
  }
  .stripes { position: absolute; inset: 0; pointer-events: none; }
  .band-mark {
    position: absolute;
    left: 748px; top: 98px; width: 250px; height: 150px;
    transform: rotate(-6deg);
    background: var(--paper);
    border-radius: 14px;
    display: flex; align-items: center; justify-content: center;
  }
  .band-mark__name {
    font-family: "Open Sans", sans-serif;
    font-weight: 600;
    font-size: 30px;
    letter-spacing: 3px;
    color: var(--ink);
  }
  .headline-live {
    position: absolute;
    left: 600px; top: 170px;
    font-family: "Rubik Wet Paint", system-ui;
    font-size: 250px;
    line-height: 1;
    color: var(--signal-red);
    letter-spacing: -4px;
  }
  .kicker {
    position: absolute;
    left: 393px; top: 410px;
    font-family: "Rubik Dirt", system-ui;
    font-size: 20px;
    color: var(--chalk);
  }
  .event-date {
    position: absolute;
    left: 548px; top: 466px;
    font-family: "Rubik Dirt", system-ui;
    font-size: 40px;
    color: var(--chalk);
    white-space: nowrap;
  }
  .event-date__time { font-size: 30px; }
  .venue {
    position: absolute;
    left: 395px; top: 534px;
    display: flex; align-items: center; gap: 10px;
    color: var(--chalk);
    white-space: nowrap;
  }
  .venue__at { font-size: 46px; line-height: 1; }
  .venue__address { font-size: 25px; }
  .highlights {
    position: absolute;
    left: 522px; top: 624px;
    transform: rotate(4deg);
    transform-origin: left top;
    font-family: "Rubik Dirt", system-ui;
    font-size: 21px;
    line-height: 1.35;
    color: var(--ink);
    white-space: nowrap;
  }
  .highlights p:nth-child(1) { padding-left: 8px; }
  .tagline {
    position: absolute;
    left: 80px; top: 759px;
    font-size: 14px;
    color: var(--signal-red);
    white-space: nowrap;
  }
  .phone {
    position: absolute;
    left: 765px; top: 738px;
    font-family: "Rubik Dirt", system-ui;
    font-size: 44px;
    color: var(--ink);
    letter-spacing: 2px;
    white-space: nowrap;
  }
</style>
</head>
<body>
<main class="flyer">
  <svg class="backdrop" width="1200" height="860" viewBox="0 0 1200 860" aria-hidden="true">
    <polygon points="57,47 1143,47 1143,660 490,590 330,730 57,730" fill="var(--night)"/>
    <polygon points="498,584 522,584 506,598" fill="var(--signal-red)"/>
    <path d="M44,790 Q300,784 600,788 T1152,792" stroke="var(--ink)" stroke-width="7" fill="none" stroke-linecap="round"/>
  </svg>

  <div class="band-photo" role="img" aria-label="Photo of the band's bass player on stage, headband on, glaring at the crowd under red and blue stage lights"></div>

  <svg class="stripes" width="1200" height="860" viewBox="0 0 1200 860" aria-hidden="true">
    <g stroke="var(--chalk)" fill="none" stroke-linecap="round">
      <path d="M57,401 L300,398 L620,402 L900,397 L1143,400" stroke-width="6"/>
      <path d="M57,463 L280,460 L540,465 L860,460 L1143,463" stroke-width="6"/>
      <path d="M57,523 L320,520 L600,525 L900,520 L1143,523" stroke-width="6"/>
      <path d="M57,587 L260,584 L480,588" stroke-width="6"/>
    </g>
  </svg>

  <div class="band-mark" role="img" aria-label="Cork Valley band logo">
    <span class="band-mark__name">CORK VALLEY</span>
  </div>

  <h1 class="headline-live">live</h1>
  <p class="kicker">grand opening on</p>
  <p class="event-date">saturday april 5th. <span class="event-date__time">7 00 pm</span></p>
  <p class="venue"><span class="venue__at">@</span><span class="venue__address">Quimby's Hall. 8241 Larkspur Ave. #204, Frisco, Texas.</span></p>

  <div class="highlights">
    <p>hottest new bar in frisco</p>
    <p>drink specials all night with</p>
    <p>the zephyr pale girls</p>
  </div>

  <p class="tagline">it's going to be a celebration fool!" and if you care for table reserved for you call now</p>
  <p class="phone">214 705 9183</p>
</main>
</body>
</html>
```